Startup Careers Fair Bunting/Banner

We'd need a bunting/banner(portrait) for an upcoming careers fair that we are going to be exhibiting at. We build innovative retail store management solutions, primarily an Vexo POS/Point of Sale on the cloud. We would like to see designs that use our primary colours of orange, black and white.

The final design should communicate a fun, exciting and attractive company to work at.

Industry/Entity Type

Retail

```html
<!DOCTYPE html>
<html lang="en">
<head>
<meta charset="utf-8">
<title>ShopNest Careers Banner</title>
<link rel="stylesheet" href="https://fonts.googleapis.com/css2?family=Roboto:wght@700;900&family=Roboto+Condensed:wght@400;700&display=swap">
<style>
  :root {
    --orange: #f7931e;
    --black: #0c0c0c;
    --white: #ffffff;
    --grey: #8a8a8a;
    --photo-light: #6b6b6b;
    --photo-dark: #2a2a2a;
  }
  html, body { margin: 0; padding: 0; overflow: hidden; background: var(--black); }
  .banner {
    position: relative;
    width: 1200px; height: 3600px;
    background: var(--black);
    overflow: hidden;
  }
  .frame {
    position: absolute; left: 80px; top: 144px;
    width: 1056px; height: 3456px;
    background: var(--orange);
    border-radius: 96px 96px 0 0;
  }
  .headline-box {
    position: absolute; left: 128px; top: 192px;
    width: 960px; height: 358px;
    background: var(--white);
    border-radius: 52px 52px 0 0;
  }
  .txt { position: absolute; margin: 0; white-space: nowrap; line-height: 1; }
  .some {
    left: 172px; top: 232px;
    font: 900 152px "Roboto", sans-serif; color: var(--orange);
    letter-spacing: 2px;
  }
  .career {
    left: 176px; top: 418px;
    font: 700 104px "Roboto Condensed", sans-serif; color: var(--black);
  }
  .for-us {
    left: 176px; top: 626px;
    font: 700 90px "Roboto Condensed", sans-serif; color: var(--white);
    letter-spacing: 2px;
  }
  .calling {
    left: 168px; top: 738px;
    font: 900 184px "Roboto", sans-serif; color: var(--black);
  }
  .cursor-icon { position: absolute; }
  .photo {
    position: absolute; left: 128px; top: 960px;
    width: 960px; height: 1328px;
    background: linear-gradient(180deg, var(--photo-dark) 0%, var(--photo-light) 55%, #3a3a3a 85%, var(--black) 100%);
  }
  .lower {
    position: absolute; left: 128px; top: 2288px;
    width: 960px; height: 1008px;
    background: var(--black);
  }
  .now-hiring {
    left: 0; width: 1200px; top: 2322px; text-align: center;
    font: 700 112px "Roboto Condensed", sans-serif; color: var(--orange);
  }
  .divider {
    position: absolute; left: 218px; width: 768px; height: 0;
    border-top: 6px dotted var(--white);
  }
  .role-list { position: absolute; left: 160px; top: 2506px; margin: 0; padding: 0; list-style: none; }
  .role {
    display: flex; align-items: center; height: 124px;
    font: 400 70px "Roboto Condensed", sans-serif; color: var(--white);
  }
  .role svg { width: 58px; height: 44px; margin-right: 30px; }
  .icons { position: absolute; top: 2990px; left: 0; width: 1200px; height: 220px; }
  .footer {
    position: absolute; left: 128px; top: 3296px;
    width: 960px; height: 304px;
    background: var(--white);
  }
  .brand { position: absolute; left: 250px; top: 3392px; display: flex; align-items: center; }
  .brand-mark { width: 118px; height: 118px; background: var(--orange); margin-right: 28px; }
  .brand-name { font: 700 124px "Roboto", sans-serif; color: var(--orange); line-height: 1; }
</style>
</head>
<body>
<div class="banner">
  <svg class="cursor-icon" style="left:1072px;top:0" width="128" height="128" viewBox="0 0 100 100">
    <polygon points="100,0 100,62 78,42 30,90 10,70 58,22 38,0" fill="var(--orange)" stroke="var(--black)" stroke-width="5"/>
  </svg>
  <div class="frame"></div>
  <div class="headline-box"></div>
  <p class="txt some">SOME</p>
  <p class="txt career">CALL IT A CAREER</p>
  <svg class="cursor-icon" style="left:910px;top:216px" width="196" height="168" viewBox="0 0 100 86">
    <polygon points="96,4 96,60 76,42 32,84 14,66 58,24 40,4" fill="var(--orange)" stroke="var(--black)" stroke-width="4"/>
  </svg>
  <p class="txt for-us">FOR US, IT’S A</p>
  <p class="txt calling">CALLING</p>

  <div class="photo" role="img" aria-label="Photo of a young man in a suit pulling his shirt open to reveal an orange emblem with two arrows on his chest"></div>

  <div class="lower"></div>
  <p class="txt now-hiring">NOW HIRING</p>
  <div class="divider" style="top:2462px"></div>
  <ul class="role-list">
    <li class="role"><svg viewBox="0 0 58 44"><polygon points="0,14 30,14 30,0 58,22 30,44 30,30 0,30" fill="var(--orange)"/></svg>Customer Service Champions</li>
    <li class="role"><svg viewBox="0 0 58 44"><polygon points="0,14 30,14 30,0 58,22 30,44 30,30 0,30" fill="var(--orange)"/></svg>Sales Warriors</li>
    <li class="role"><svg viewBox="0 0 58 44"><polygon points="0,14 30,14 30,0 58,22 30,44 30,30 0,30" fill="var(--orange)"/></svg>Online Marketing Ninjas</li>
  </ul>
  <div class="divider" style="top:2884px"></div>

  <svg class="icons" viewBox="0 0 1200 220">
    <g fill="var(--grey)">
      <path d="M255,150 a40,40 0 0 1 18,-72 a62,62 0 0 1 116,-10 a46,46 0 0 1 64,46 a36,36 0 0 1 -8,36 z"/>
      <rect x="600" y="40" width="112" height="60" rx="6"/>
      <rect x="660" y="20" width="40" height="22" rx="4"/>
      <rect x="572" y="100" width="168" height="100" rx="8"/>
      <g fill="var(--black)">
        <rect x="612" y="52" width="88" height="30"/>
        <rect x="592" y="116" width="24" height="16"/><rect x="624" y="116" width="24" height="16"/><rect x="656" y="116" width="24" height="16"/>
        <rect x="592" y="140" width="24" height="16"/><rect x="624" y="140" width="24" height="16"/><rect x="656" y="140" width="24" height="16"/>
        <rect x="690" y="116" width="32" height="40"/>
        <rect x="592" y="170" width="130" height="14"/>
      </g>
      <rect x="822" y="10" width="128" height="208" rx="18"/>
      <rect x="836" y="36" width="100" height="152" fill="var(--black)"/>
      <circle cx="886" cy="203" r="8" fill="var(--black)"/>
    </g>
  </svg>

  <div class="footer"></div>
  <div class="brand">
    <div class="brand-mark"></div>
    <span class="brand-name">ShopNest</span>
  </div>
</div>
</body>
</html>
```